Executive Business Card for Healthcare Company [Need Today]

I need a business card design for a healthcare company. The only branding the company has thus far is a logo. The cards will be utilized by company executives. The design I envision will be vibrant and appealing but with a corporate feel. They shouldn't be too casual or playful. I would like to complete this project TODAY if possible.

Target Market(s)

Healthcare vendors, other executives in healthcare and pharmaceuticals

Industry/Entity Type

Pharmaceutical

Contact Information for Business Card

See attachment

Font styles to use
Serif
Sans Serif

Colors

Designer to choose colors to be used in the design.

```html
<!DOCTYPE html>
<html lang="en">
<head>
<meta charset="utf-8">
<title>Corvane Therapeutics – Executive Business Card</title>
<link href="https://fonts.googleapis.com/css2?family=Open+Sans:wght@400;600&display=swap" rel="stylesheet">
<style>
  :root {
    --bg: #ececea;
    --teal: #34c1c6;
    --teal-light: #4fd8dc;
    --teal-deep: #1fa3a8;
    --green: #4cb27a;
    --name: #3cbfae;
    --ink: #4a4f52;
    --muted: #8a9093;
    --white: #ffffff;
  }
  * { box-sizing: border-box; margin: 0; padding: 0; }
  html, body { width: 1200px; height: 800px; overflow: hidden; }
  body {
    background: var(--bg);
    font-family: "Open Sans", sans-serif;
    display: flex;
    flex-direction: column;
    align-items: center;
    justify-content: center;
    gap: 48px;
  }
  .card {
    position: relative;
    width: 560px;
    height: 320px;
    border-radius: 22px;
    overflow: hidden;
    box-shadow: 0 10px 28px rgba(0,0,0,0.18);
  }
  /* Front */
  .card--front {
    background: linear-gradient(160deg, var(--teal-light) 0%, var(--teal) 55%, var(--teal-deep) 100%);
    display: flex;
    align-items: center;
    justify-content: center;
  }
  .brand {
    display: flex;
    align-items: center;
    gap: 16px;
  }
  .brand__dot {
    border-radius: 50%;
    border: 3px solid currentColor;
    flex: none;
  }
  .brand__name {
    font-weight: 400;
    line-height: 1.05;
    letter-spacing: 0.5px;
  }
  .card--front .brand { color: var(--white); }
  .card--front .brand__dot { width: 82px; height: 82px; }
  .card--front .brand__name { font-size: 40px; }
  .card--front .brand__name small { display: block; font-size: 22px; }

  /* Back */
  .card--back { background: var(--white); }
  .card--back .brand {
    position: absolute;
    left: 34px;
    top: 30px;
    color: var(--teal);
    gap: 12px;
  }
  .card--back .brand__dot { width: 54px; height: 54px; border-width: 2px; }
  .card--back .brand__name { font-size: 26px; }
  .card--back .brand__name small { display: block; font-size: 15px; }

  .person {
    position: absolute;
    right: 30px;
    top: 84px;
    width: 228px;
    z-index: 1;
  }
  .person__name {
    font-size: 26px;
    line-height: 1.2;
    font-weight: 600;
    color: var(--name);
    letter-spacing: 0.5px;
  }
  .person__title {
    font-size: 12px;
    line-height: 1.4;
    color: var(--muted);
    letter-spacing: 0.6px;
    margin-bottom: 10px;
  }
  .contact { list-style: none; }
  .contact li {
    display: flex;
    align-items: center;
    gap: 12px;
    font-size: 15px;
    line-height: 20px;
    color: var(--ink);
    margin-bottom: 5px;
  }
  .contact svg { width: 18px; height: 18px; flex: none; }

  .wave {
    position: absolute;
    left: 0;
    bottom: 0;
    width: 560px;
    height: 320px;
  }
  .address {
    position: absolute;
    left: 46px;
    bottom: 20px;
    font-size: 15px;
    font-style: normal;
    line-height: 1.2;
    color: var(--white);
  }
</style>
</head>
<body>

  <section class="card card--front" aria-label="Card front">
    <div class="brand">
      <span class="brand__dot"></span>
      <p class="brand__name">corvane<small>therapeutics</small></p>
    </div>
  </section>

  <section class="card card--back" aria-label="Card back">
    <svg class="wave" viewBox="0 0 560 320" aria-hidden="true">
      <path d="M0,180 C120,176 230,196 310,232 S440,282 560,280" fill="none" stroke="var(--teal)" stroke-width="4"/>
      <path d="M0,188 C120,184 230,204 310,240 S440,290 560,288" fill="none" stroke="var(--green)" stroke-width="5"/>
      <path d="M0,200 C120,196 225,218 300,252 S430,302 560,300 L560,320 L0,320 Z" fill="var(--teal)"/>
    </svg>

    <div class="brand">
      <span class="brand__dot"></span>
      <p class="brand__name">corvane<small>therapeutics</small></p>
    </div>

    <div class="person">
      <h1 class="person__name">Daniel Morrow</h1>
      <p class="person__title">Senior Director of Marketing</p>
      <ul class="contact">
        <li>
          <svg viewBox="0 0 18 18" aria-hidden="true"><circle cx="9" cy="9" r="9" fill="var(--green)"/><path d="M6 5 L7.5 5 L8.3 7 L7.3 7.8 C7.8 9 8.9 10.2 10.2 10.7 L11 9.7 L13 10.5 L13 12 C13 12.6 12.5 13 12 13 C8.5 12.8 5.2 9.5 5 6 C5 5.5 5.4 5 6 5 Z" fill="var(--white)"/></svg>
          555-201-4817
        </li>
        <li>
          <svg viewBox="0 0 18 18" aria-hidden="true"><circle cx="9" cy="9" r="9" fill="var(--green)"/><rect x="4.5" y="6" width="9" height="6.5" rx="0.8" fill="none" stroke="var(--white)" stroke-width="1.2"/><path d="M4.8 6.4 L9 9.6 L13.2 6.4" fill="none" stroke="var(--white)" stroke-width="1.2"/></svg>
          dmorrow@corvanerx.com
        </li>
        <li>
          <svg viewBox="0 0 18 18" aria-hidden="true"><circle cx="9" cy="9" r="9" fill="var(--green)"/><rect x="6.3" y="4" width="5.4" height="10" rx="1" fill="none" stroke="var(--white)" stroke-width="1.2"/><circle cx="9" cy="12" r="0.7" fill="var(--white)"/></svg>
          555-308-6142
        </li>
      </ul>
    </div>

    <address class="address">
      Corvane Therapeutics, LLC<br>
      118 Linden Park Avenue<br>
      Millbrook, GA 30999
    </address>
  </section>

</body>
</html>
```